Hollin Reach (we have a logo but are open to options ) (we hand make 100% soy candles & other hom

See our webpage for ideas www.hollinreach.com.
We need packaging for our Universal Jars in 5 different fragrances to start with & need to be able to add new lines along the way.
The box needs to be uniformed and then adding what is required to reflect each fragrance as we add them on the line. Eg. Midnight Orchard, Pear & Cedar, Nordic Heather, Sandal & Plum, Calm Peppermint (&; these could change).
There will also be matching boxes required for Reed Diffusers, Tealights and so on in our range.
-We want a white box, with a lux look, and kept simple. (We think an embossed logo might give it that lux look).
-We need to add things to our box like, warning instructions, burn instructions, barcodes etc.
-We are also changing our instragram account with our colour palette which will be backgrounds of white and pastel pinks, pink shades, some grey & black.
It's a chic lux sophicated look! Thank you.
16/06/18 We have just updated this brief. I have attached a colour palette picture. Ideally we would like the box to be white with embossed logo and maybe textured print on the sides or a chic print on the sides. The whole box appears to be too busy. It needs to look more feminine. On the colour palette, those colours could be used to write each different fragrance or the fragrance could be written in those colours. We hope this makes sense. We look forward to working with someone and hopefully we can use Skye or facetime to explain ourselves better. :)
Many Thanks, we hope you have fun with it.

Target Market(s)

People between ages of 18 to 50

Industry/Entity Type

Retail

Font styles to use
Sans Serif

Colors
ffffff
e667a6
eda3c7
f9d9e8
fdf0f6
959595
dbdbdb

Requirements
Must have
• Lux look with nice clean lines keeping it simple
• Obvioulsy, colours will change slightly when the box is introduced with a new fragrance to suit. Eg. Calm Peppermint (yellow /green)
Nice to have
• Pattern for the fragrance to differ the uniformity of the boxes to the brand.
• 100% Soy Wax.

```html
<!DOCTYPE html>
<html lang="en">
<head>
<meta charset="utf-8">
<title>Hollin Reach – Nordic Heather Packaging</title>
<link href="https://fonts.googleapis.com/css2?family=Montserrat:wght@300;400;500&display=swap" rel="stylesheet">
<style>
  :root {
    --canvas: #ececec;
    --box-white: #ffffff;
    --pink-blush: #fdf0f6;
    --pink-soft: #f9d9e8;
    --pink-mid: #eda3c7;
    --pink-deep: #e667a6;
    --grey-mid: #959595;
    --grey-light: #dbdbdb;
  }
  * { margin: 0; padding: 0; box-sizing: border-box; }
  html, body {
    width: 1200px; height: 800px; overflow: hidden;
    background: var(--canvas);
    font-family: "Montserrat", sans-serif;
  }
  .layout {
    position: relative; width: 1200px; height: 800px;
    display: flex; align-items: center; justify-content: center; gap: 80px;
  }

  /* Box front panel */
  .box-face {
    position: relative; width: 460px; height: 460px;
    background: var(--box-white);
    border: 1px solid var(--grey-light);
  }
  .box-face .tagline {
    position: absolute; top: 40px; left: 0; right: 0;
    text-align: center; font-size: 11px; font-weight: 300;
    line-height: 1.5; letter-spacing: 0.02em; color: var(--grey-mid);
  }
  .box-face .brand-disc {
    position: absolute; left: 58px; top: 96px;
    width: 290px; height: 300px; border-radius: 50%;
    background: var(--pink-soft);
    display: flex; align-items: center; justify-content: center;
  }
  .brand-name {
    font-weight: 400; letter-spacing: 0.22em; text-transform: uppercase;
    color: var(--pink-deep);
    display: flex; align-items: center; gap: 8px; white-space: nowrap;
  }
  .brand-name .mark {
    width: 6px; height: 6px; border-radius: 50%; background: var(--pink-deep);
  }
  .box-face .brand-name { font-size: 15px; }
  .box-face .fragrance {
    position: absolute; right: 34px; bottom: 74px;
    text-align: right; font-size: 13px; font-weight: 500; line-height: 1.35;
    color: var(--pink-deep);
  }
  .box-face .spec {
    position: absolute; right: 34px; bottom: 30px;
    text-align: right; font-size: 9px; font-weight: 300; line-height: 1.5;
    color: var(--grey-mid);
  }

  /* Jar label */
  .jar-label {
    position: relative; width: 400px; height: 360px;
    background: var(--box-white);
    border: 1px solid var(--grey-light);
    display: flex; align-items: center; justify-content: center;
  }
  .jar-label .label-field {
    position: relative; width: 330px; height: 290px;
    background: var(--pink-blush); border-radius: 26px;
  }
  .jar-label .label-blob {
    position: absolute; left: 45px; top: 50px; width: 240px; height: 170px;
  }
  .jar-label .label-brand {
    position: absolute; left: 45px; top: 50px; width: 240px; height: 170px;
    display: flex; align-items: center; justify-content: center;
  }
  .jar-label .brand-name { font-size: 12px; }
  .jar-label .fragrance {
    position: absolute; right: 20px; bottom: 20px;
    text-align: right; font-size: 11px; font-weight: 500; line-height: 1.35;
    color: var(--pink-deep);
  }
</style>
</head>
<body>
  <main class="layout">
    <section class="box-face" aria-label="Candle box front">
      <p class="tagline">Australian<br>made &amp;<br>hand poured</p>
      <div class="brand-disc">
        <span class="brand-name"><span class="mark"></span>Hollin Reach</span>
      </div>
      <p class="fragrance">Nordic<br>Heather</p>
      <p class="spec">100% Soy Candle<br>340 G</p>
    </section>

    <section class="jar-label" aria-label="Candle jar label">
      <div class="label-field">
        <svg class="label-blob" viewBox="0 0 240 170" aria-hidden="true">
          <path d="M30 38 C55 6 185 2 215 36 C240 62 232 132 200 152 C165 174 70 172 38 150 C8 130 6 66 30 38 Z" fill="#f9d9e8"/>
        </svg>
        <div class="label-brand">
          <span class="brand-name"><span class="mark"></span>Hollin Reach</span>
        </div>
        <p class="fragrance">Nordic<br>Heather</p>
      </div>
    </section>
  </main>
</body>
</html>
```